Buchcover-Design für Fantasy-Serie
Inspirierte und saubere Umsetzung, sowie kundenorientiert auch bei Sonderwünschen.
Zielgruppe
Buchverlag (Kleinstverlag). Wir verlegen Bücher aus den Genres Fantasy / SciFi / Thriller und Kriminalroman, sowie spezielle thematische Ausgaben. Kern unserer Tätigkeit ist die Wiederveröffentlichung der Nebelhorn-Chronik des deutschen Fantasy Autors Konrad Tilling sowie eine SciFi Serie des deutschen Autor Enno Braxmeyer. Wir suchen genretypische Cover mit Whow-Effekt.
Aufgabenstellung
Bei unserem ersten Auftrag handelt es sich um eine Fantasy Serie, bestehend aus 8 Bänden, welche vorwiegend als Kindle / eBook aber auch als Paperback veröffentlicht werden. Das Titelmotiv stammt jedes Mal von Laurent Dubelcq (lizensiert) und ändert sich bei jedem Buch. Der Titel muss daher von uns bearbeitbar sein.
das EBook hat die üblichen Maße: 1600x2560, 72 dpi
Print wird voraussichtl. 12x19, aber wir benötigen nur den Titel in 300 DPI (identisch mit Ebook lediglich höhere Auflösung).
Text:
(Autorenname): Konrad Tilling
(Buchtitel): Der Zirkel von Quasmar
(Titelzusatz): Erster Roman der Nebelhorn-Chronik
(Gattung): Roman
(Verlagslogo): Wahlweise kleines oder großes Logo, farblich angepasst
Hinweis: bei Auftrag wird das Titelbild in hoher Auflösung von uns geliefert.

```html
<!DOCTYPE html>
<html lang="de">
<head>
<meta charset="utf-8">
<title>Der Zirkel von Quasmar – Cover</title>
<link href="https://fonts.googleapis.com/css2?family=Marcellus&family=Cinzel:wght@600&family=Lato:wght@400&family=Oswald:wght@400;600&family=Roboto+Slab:wght@500&family=Noto+Serif&display=swap" rel="stylesheet">
<style>
  :root {
    --stage: #b3b3b3;
    --night: #11151f;
    --deep-blue: #0c1f38;
    --spine-blue: #0c3654;
    --accent: #1aa3e8;
    --white: #ffffff;
    --line: #6f93b3;
  }
  * { margin: 0; padding: 0; box-sizing: border-box; }
  html, body { width: 1200px; height: 1200px; overflow: hidden; background: var(--stage); }
  .wrap { position: absolute; left: 110px; top: 236px; width: 979px; height: 726px; box-shadow: 0 2px 6px rgba(0,0,0,.25); }

  .back {
    position: absolute; left: 0; top: 0; width: 460px; height: 726px;
    background:
      radial-gradient(ellipse 160px 90px at 120px 560px, rgba(150,170,205,.55), transparent 70%),
      radial-gradient(ellipse 120px 80px at 350px 640px, rgba(130,150,190,.4), transparent 70%),
      radial-gradient(ellipse 200px 140px at 220px 260px, rgba(90,115,160,.35), transparent 70%),
      linear-gradient(180deg, var(--night) 0%, var(--deep-blue) 55%, #13294a 100%);
  }
  .spine { position: absolute; left: 460px; top: 0; width: 60px; height: 726px; background: var(--spine-blue); border-left: 1px solid #2d6a93; border-right: 1px solid #2d6a93; }
  .front {
    position: absolute; left: 520px; top: 0; width: 459px; height: 726px;
    background: linear-gradient(180deg, #12161f 0%, #161d2b 35%, #1f2d42 100%);
  }
  .front-art {
    position: absolute; left: 0; top: 330px; width: 459px; height: 396px;
    background:
      radial-gradient(ellipse 160px 120px at 130px 130px, rgba(175,195,220,.55), transparent 70%),
      radial-gradient(ellipse 120px 60px at 380px 340px, rgba(220,230,240,.45), transparent 70%),
      linear-gradient(180deg, rgba(22,29,43,0) 0%, #3b4d63 45%, #2a3b44 75%, #1e2c30 100%);
  }

  .imprint { font-family: "Cinzel", serif; font-weight: 600; color: var(--white); letter-spacing: 1px; position: absolute; text-align: center; }

  .back .imprint { left: 0; width: 474px; top: 214px; font-size: 17px; }
  .blurb {
    position: absolute; left: 99px; top: 246px; width: 278px; height: 266px;
    background: rgba(12,54,84,.88); border: 1px solid #4f7ea3;
    border-radius: 24px 0 24px 0; padding: 17px 18px 0 18px; overflow: hidden;
    font-family: "Noto Serif", serif; font-size: 9.2px; line-height: 13.8px; letter-spacing: -0.1px;
    color: var(--white); text-align: justify;
  }
  .blurb p + p { margin-top: 13.8px; }

  .spine-title {
    position: absolute; left: 16px; top: 56px; writing-mode: vertical-rl;
    font-family: "Lato", sans-serif; font-size: 26px; letter-spacing: 5.5px; color: var(--white);
  }
  .spine-title .blue { color: var(--accent); }
  .spine-author {
    position: absolute; left: 16px; top: 578px; width: 23px; height: 116px;
    border: 1px solid #8fb2cc; writing-mode: vertical-rl;
    font-family: "Roboto Slab", serif; font-size: 10.5px; letter-spacing: 1.2px; color: var(--white);
    display: flex; align-items: center; justify-content: center;
  }
  .spine-author-label { position: absolute; left: 38px; top: 624px; writing-mode: vertical-rl; font-family: "Oswald", sans-serif; font-size: 8px; letter-spacing: 1px; color: var(--accent); background: var(--spine-blue); padding: 2px 0; }

  .front .imprint { left: 0; width: 459px; top: 50px; font-size: 21px; }
  .title { position: absolute; left: 0; width: 459px; top: 114px; text-align: center; color: var(--white); font-weight: normal; }
  .title .t1 { font-family: "Marcellus", serif; font-size: 36px; line-height: 36px; letter-spacing: 2px; }
  .title .t2 { font-family: "Marcellus", serif; font-size: 37px; line-height: 38px; letter-spacing: 5px; }
  .title .t3 { font-family: "Lato", sans-serif; font-size: 36px; line-height: 36px; color: var(--accent); }
  .series { position: absolute; left: 0; width: 459px; top: 262px; text-align: center; }
  .series .pre { font-family: "Oswald", sans-serif; font-size: 17px; letter-spacing: 1.5px; color: var(--accent); }
  .series .name { font-family: "Oswald", sans-serif; font-size: 25px; letter-spacing: 10px; color: var(--white); margin-top: 2px; }
  .series .tail { display: flex; align-items: center; justify-content: center; gap: 12px; margin-top: -2px; }
  .series .tail span { font-family: "Oswald", sans-serif; font-weight: 600; font-size: 22px; color: var(--accent); }
  .series .tail i { display: block; width: 54px; height: 1px; background: var(--accent); }
  .author { position: absolute; left: 129px; top: 634px; width: 207px; height: 43px; border: 1px solid #c9d5df; display: flex; align-items: center; justify-content: center; font-family: "Roboto Slab", serif; font-size: 19px; letter-spacing: 2.5px; color: var(--white); }
  .author-label { position: absolute; left: 0; width: 459px; top: 620px; text-align: center; }
  .author-label span { font-family: "Oswald", sans-serif; font-size: 17px; letter-spacing: 1.5px; color: var(--accent); background: #2c3b4a; padding: 0 6px; }
</style>
</head>
<body>
<div class="wrap">
  <section class="back">
    <div class="imprint">VELMORAN</div>
    <div class="blurb">
      <p>Lorem ipsum dolor sit amet, consectetuer adipiscing elit, sed diam nonummy nibh euismod tincidunt ut laoreet dolore magna aliquam erat volutpat. Ut wisi enim ad minim veniam, quis nostrud exerci tation ullamcorper suscipit lobortis nisl ut aliquip ex ea commodo consequat. Duis autem vel eum iriure dolor in hendrerit in vulputate velit esse molestie consequat, vel illum dolore eu feugiat nulla facili</p>
      <p>Lorem ipsum dolor sit amet, consectetuer adipiscing elit, sed diam nonummy nibh euismod tincidunt ut laoreet dolore magna aliquam erat volutpat. Ut wisi enim ad minim veniam, quis nostrud exerci tation ullamcorper suscipit lobortis nisl ut aliquip ex ea commodo consequat. Duis autem vel eum iriure dolor in hendrerit in vulputate velit esse molestie consequat, vel illum dolore eu feugiat nulla facili</p>
    </div>
  </section>

  <section class="spine">
    <div class="spine-title">DER ZIRKEL <span class="blue">VON QUASMAR</span></div>
    <div class="spine-author">Konrad Tilling</div>
    <div class="spine-author-label">Author</div>
  </section>

  <section class="front">
    <div class="front-art" role="img" aria-label="Titelillustration: stürmischer Himmel über gewaltigen Felsformationen und verschneiten Klippen mit Tannen"></div>
    <div class="imprint">VELMORAN</div>
    <h1 class="title">
      <div class="t1">DER</div>
      <div class="t2">ZIRKEL</div>
      <div class="t3">VON QUASMAR</div>
    </h1>
    <div class="series">
      <div class="pre">Erster Roman der</div>
      <div class="name">Nebelhorn</div>
      <div class="tail"><i></i><span>-Chronik</span><i></i></div>
    </div>
    <div class="author">Konrad Tilling</div>
    <div class="author-label"><span>Author</span></div>
  </section>
</div>
</body>
</html>
```